Stationery Design Project

Minimal Design. Black and White Colours Only.
Need Business Card
With Compliments slip
Letterhead
A4 Folder

Target Market(s)

Luxury architectual designed home owners

Industry/Entity Type

Business

Requirements
Must have
• Black and White colours only. Suggest some good textured stock for business card for future printing. try to use font that is used in my logo our some other minimal modern font.

```html
<!DOCTYPE html>
<html lang="en">
<head>
<meta charset="utf-8">
<title>Halden Estates – Business Card</title>
<link href="https://fonts.googleapis.com/css2?family=Arimo:wght@400;700&display=swap" rel="stylesheet">
<style>
  :root {
    --ink: #111111;
    --paper: #ffffff;
    --edge-dark: #8a8a8a;
    --edge-light: #c8c8c8;
    --tone-deep: #5a5a5a;
    --tone-soft: #d4d4d4;
  }
  html, body {
    margin: 0;
    padding: 0;
    width: 1200px;
    height: 390px;
    overflow: hidden;
    background: var(--paper);
    font-family: "Arimo", Arial, sans-serif;
    color: var(--ink);
  }
  .sheet { position: relative; width: 1200px; height: 390px; }
  .card {
    position: absolute;
    top: 8px;
    height: 374px;
    background: var(--paper);
    box-sizing: border-box;
    overflow: hidden;
  }
  .card--front { left: 8px; width: 588px; border: 1.5px solid var(--edge-dark); }
  .card--back { left: 614px; width: 580px; border: 1.5px solid var(--edge-light); border-radius: 6px; }

  .ornament-area {
    position: absolute;
    background: linear-gradient(135deg, var(--tone-deep), var(--tone-soft));
  }
  .ornament-area--front-right { left: 446px; top: 0; width: 142px; height: 374px; }
  .ornament-area--back-top { left: 0; top: 0; width: 400px; height: 92px; }
  .ornament-area--back-corner { left: 500px; top: 272px; width: 80px; height: 102px; }

  .brand {
    position: absolute;
    display: flex;
    align-items: center;
    font-weight: 700;
    white-space: nowrap;
  }
  .brand__mark { background: var(--ink); display: inline-block; }
  .brand--small { left: 54px; top: 30px; font-size: 18px; gap: 10px; }
  .brand--small .brand__mark { width: 24px; height: 24px; }
  .brand--large { left: 40px; top: 118px; font-size: 30px; gap: 16px; }
  .brand--large .brand__mark { width: 46px; height: 46px; }

  .person {
    position: absolute;
    left: 230px;
    top: 78px;
    width: 220px;
    text-align: center;
    font-size: 20px;
    line-height: 38px;
  }
  .contacts {
    position: absolute;
    left: 30px;
    top: 168px;
    font-size: 20px;
    line-height: 36px;
  }
  .address {
    position: absolute;
    left: 172px;
    top: 190px;
    font-size: 20px;
    line-height: 30px;
  }
  .website {
    position: absolute;
    left: 0;
    width: 560px;
    top: 300px;
    text-align: center;
    font-size: 20px;
  }
</style>
</head>
<body>
<main class="sheet">
  <section class="card card--front">
    <div class="ornament-area ornament-area--front-right" role="img" aria-label="Decorative flowing line ribbon along the right side"></div>
    <div class="brand brand--small"><span class="brand__mark"></span>HALDEN ESTATES</div>
    <div class="person">
      <div class="person__name">Marcus Halden</div>
      <div class="person__title">Managing Director</div>
    </div>
    <div class="contacts">
      <div class="contacts__mobile">M: +61 400 555 123</div>
      <div class="contacts__phone">P: +61 7 3000 4567</div>
      <div class="contacts__email">mhalden@haldenestates.com</div>
    </div>
  </section>

  <section class="card card--back">
    <div class="ornament-area ornament-area--back-top" role="img" aria-label="Decorative flowing line ribbon across the top left"></div>
    <div class="ornament-area ornament-area--back-corner" role="img" aria-label="Decorative flowing line ribbon in the bottom right corner"></div>
    <div class="brand brand--large"><span class="brand__mark"></span>HALDEN ESTATES</div>
    <div class="address">
      <div>level 12, 40 Harbour st</div>
      <div>Brisbane QLD 4000 Australia</div>
    </div>
    <div class="website">haldenestates.com</div>
  </section>
</main>
</body>
</html>
```